Front and back of folded card is black. Front has your logo design in gold ink.Inside panel says Fellowship of the Quiet Lantern.org Recovery is GoldenBack of card, says Rev. Dr. Zoli Althea Brownegold ink This is for folks facing their shadow work in the recovery process from addictions. I see this: A black dove heading down into an open rose with thorns and a cross.

Target Market(s)

addiction recovery

Contact Information for Business Card

The card will be folded. Outside front panel has logo
Inside panel has copy and back side has copy

Logo Text

Dark purple dove flying into open rose with thorns , include a cross in the design

Font styles to use
Script

Colors
fbed22
6b449b
33a6d7

Requirements
Must have
• Legible script font...beautiful, hopeful, serious.
Should not have
• silly or overdone theme

```html
<!DOCTYPE html>
<html lang="en">
<head>
<meta charset="utf-8">
<title>Fellowship of the Quiet Lantern — Logo and Folded Card</title>
<link rel="stylesheet" href="https://fonts.googleapis.com/css2?family=Great+Vibes&family=Cormorant+Garamond:ital,wght@1,600&family=Open+Sans:wght@400;600&display=swap">
<style>
  :root {
    --page: #dcdcdc;
    --card-black: #141414;
    --logo-black: #000000;
    --gold: #d9a520;
    --gold-light: #f0c640;
    --fold: #2a2a2a;
    --label: #111111;
    --rose-red: #7a0f14;
    --rose-dark: #1a0506;
  }
  * { box-sizing: border-box; margin: 0; padding: 0; }
  html, body {
    width: 1200px; height: 900px; overflow: hidden;
    background: var(--page);
    font-family: "Open Sans", Arial, sans-serif;
  }
  .canvas { position: relative; width: 1200px; height: 900px; }

  /* Logo presentation */
  .logo-panel {
    position: absolute; left: 0; top: 0; width: 400px; height: 240px;
    background: var(--logo-black);
    display: flex; flex-direction: column; align-items: center; justify-content: center; gap: 16px;
  }
  .brand-dot {
    width: 120px; height: 120px; border-radius: 50%;
    background: var(--gold);
  }
  .brand-name {
    font-family: "Open Sans", Arial, sans-serif; font-weight: 600;
    color: var(--gold); font-size: 22px; letter-spacing: 0.3px;
  }
  .section-label {
    position: absolute; font-size: 26px; color: var(--label); font-weight: 400;
  }
  .section-label--logo { left: 120px; top: 244px; }
  .section-label--card { left: 92px; top: 706px; }

  /* Folded card spreads */
  .spread {
    position: absolute; left: 440px; width: 720px; height: 206px;
    display: flex; box-shadow: 0 10px 24px rgba(0,0,0,0.18);
  }
  .spread--outside { top: 290px; }
  .spread--inside { top: 560px; }
  .panel {
    position: relative; width: 360px; height: 206px;
    background: var(--card-black);
    display: flex; flex-direction: column; align-items: center; justify-content: center;
  }
  .panel + .panel { border-left: 1px solid var(--fold); }

  .tagline {
    font-family: "Great Vibes", cursive; color: var(--gold);
    font-size: 40px; line-height: 1;
  }
  .web-address {
    margin-top: 14px; font-size: 11.5px; color: var(--gold); letter-spacing: 0.3px;
  }
  .panel--front { gap: 14px; }
  .panel--front .brand-dot { width: 84px; height: 84px; }
  .panel--front .brand-name { font-size: 17px; }

  .minister-name {
    font-family: "Cormorant Garamond", Georgia, serif; font-style: italic; font-weight: 600;
    color: var(--gold); font-size: 25px;
  }
  .mission {
    margin-top: 18px; width: 280px; text-align: center;
    font-size: 11.5px; line-height: 1.4; color: var(--gold);
  }
  .panel--artwork {
    background:
      radial-gradient(ellipse at 50% 30%, rgba(240,240,240,0.35) 0, rgba(240,240,240,0) 22%),
      linear-gradient(180deg, var(--card-black) 0%, var(--rose-dark) 45%, var(--rose-red) 100%);
  }
</style>
</head>
<body>
<main class="canvas">
  <section class="logo-panel">
    <div class="brand-dot"></div>
    <p class="brand-name">Fellowship of the Quiet Lantern</p>
  </section>
  <p class="section-label section-label--logo">Logo Design</p>

  <section class="spread spread--outside">
    <div class="panel panel--back">
      <p class="tagline">Healing is Steady</p>
      <p class="web-address">FellowshipoftheQuietLantern.org</p>
    </div>
    <div class="panel panel--front">
      <div class="brand-dot"></div>
      <p class="brand-name">Fellowship of the Quiet Lantern</p>
    </div>
  </section>

  <section class="spread spread--inside">
    <div class="panel panel--minister">
      <p class="minister-name">Rev. Dr. Mirela Quinta Hartwick</p>
      <p class="mission">This is for folks facing their shadow work in the recovery process from addictions</p>
    </div>
    <div class="panel panel--artwork" role="img" aria-label="Photo of a white dove flying above red roses with thorny stems on black"></div>
  </section>
  <p class="section-label section-label--card">Business Card Design</p>
</main>
</body>
</html>
```